Wellspring Care Alliance Vonzo Ads

We want an ad created for the gay dating app vonzo. The size is 300x250. We want the ad to be sexy, with a shirtless man. We are advertising our free HIV and PrEP services. We are open to slogans about maybe "Bringing HIV and PrEP To You"
"Free PrEP and HIV Management"
Open to ideas.

We also offer through the Harborlight Support Fund
Copay Assistance, Insurance Premium Assistance, Free Medical Services, etc
Our website is wcanj.org

I do want the ad to have a Book Now Button

Gay sexually active males

```html
<!DOCTYPE html>
<html lang="en">
<head>
<meta charset="utf-8">
<title>Wellspring Care Alliance – Free PrEP Ads</title>
<link rel="stylesheet" href="https://fonts.googleapis.com/css2?family=Roboto:wght@500;700;900&display=swap">
<style>
  :root {
    --page-bg: #000000;
    --ad-white: #ffffff;
    --headline-pink: #ec4a90;
    --headline-edge: #5b1a3a;
    --body-maroon: #5a1d3a;
    --brand-blue: #3d4fc4;
    --brand-dot: #9a5bd6;
    --button-top: #4a4a4a;
    --button-bottom: #0c0c0c;
    --button-text: #ffffff;
    --skin-light: #c59a80;
    --skin-mid: #8a5a40;
    --skin-dark: #4a2e22;
  }
  * { box-sizing: border-box; margin: 0; padding: 0; }
  html, body {
    width: 1200px;
    height: 526px;
    overflow: hidden;
    background: var(--page-bg);
    font-family: "Roboto", Arial, sans-serif;
  }
  .stage {
    position: relative;
    width: 1200px;
    height: 526px;
  }
  .ad {
    position: absolute;
    top: 44px;
    width: 565px;
    height: 435px;
    background: var(--ad-white);
    overflow: hidden;
  }
  .ad--first { left: 26px; }
  .ad--second { left: 623px; width: 552px; }

  .ad__photo {
    position: absolute;
    left: 0;
    top: 0;
    width: 72%;
    height: 100%;
  }
  .ad--first .ad__photo {
    background:
      linear-gradient(90deg, rgba(255,255,255,0) 45%, var(--ad-white) 100%),
      radial-gradient(ellipse at 30% 40%, var(--skin-light) 0%, var(--skin-mid) 55%, var(--skin-dark) 100%);
  }
  .ad--second .ad__photo {
    background:
      linear-gradient(90deg, rgba(255,255,255,0) 45%, var(--ad-white) 100%),
      radial-gradient(ellipse at 40% 45%, var(--skin-mid) 0%, var(--skin-dark) 60%, #1e1612 100%);
  }

  .ad__content {
    position: absolute;
    right: 22px;
    top: 0;
    width: 300px;
    height: 100%;
  }

  .brand {
    position: absolute;
    right: 0;
    top: 22px;
    display: flex;
    align-items: center;
    gap: 12px;
  }
  .brand__dot {
    width: 52px;
    height: 52px;
    border-radius: 50%;
    background: var(--brand-dot);
  }
  .brand__name {
    color: var(--brand-blue);
    font-weight: 700;
    font-size: 19px;
    line-height: 1.1;
    width: 140px;
  }

  .headline {
    position: absolute;
    right: 0;
    top: 118px;
    text-align: right;
    color: var(--headline-pink);
    font-weight: 900;
    line-height: 1.04;
    -webkit-text-stroke: 1px var(--headline-edge);
  }
  .headline__free { display: block; font-size: 44px; }
  .headline__line { display: block; font-size: 40px; white-space: nowrap; }

  .body-copy {
    position: absolute;
    right: 0;
    top: 262px;
    width: 270px;
    color: var(--body-maroon);
    font-weight: 500;
    font-size: 15.5px;
    line-height: 1.2;
    text-align: justify;
  }

  .book-button {
    position: absolute;
    right: 0;
    top: 356px;
    width: 128px;
    height: 44px;
    border-radius: 10px;
    background: linear-gradient(180deg, var(--button-top), var(--button-bottom));
    color: var(--button-text);
    font-weight: 700;
    font-size: 18px;
    display: flex;
    align-items: center;
    justify-content: center;
    letter-spacing: 0.3px;
  }
</style>
</head>
<body>
<main class="stage">

  <section class="ad ad--first">
    <div class="ad__photo" role="img" aria-label="Close-up photo of a shirtless man lying on white sheets"></div>
    <div class="ad__content">
      <div class="brand">
        <span class="brand__dot"></span>
        <span class="brand__name">Wellspring Care Alliance</span>
      </div>
      <h1 class="headline">
        <span class="headline__free">FREE</span>
        <span class="headline__line">PrEP and HIV</span>
        <span class="headline__line">Management</span>
      </h1>
      <p class="body-copy">We offer Harborlight Support Fund, a program made possible by the savings generated through the 340B Drug Pricing Program</p>
      <div class="book-button">BOOK NOW</div>
    </div>
  </section>

  <section class="ad ad--second">
    <div class="ad__photo" role="img" aria-label="Photo of a shirtless man sitting in jeans, hand raised to his face"></div>
    <div class="ad__content">
      <div class="brand">
        <span class="brand__dot"></span>
        <span class="brand__name">Wellspring Care Alliance</span>
      </div>
      <h1 class="headline">
        <span class="headline__free">FREE</span>
        <span class="headline__line">PrEP and HIV</span>
        <span class="headline__line">Management</span>
      </h1>
      <p class="body-copy">We offer Harborlight Support Fund, a program made possible by the savings generated through the 340B Drug Pricing Program</p>
      <div class="book-button">BOOK NOW</div>
    </div>
  </section>

</main>
</body>
</html>
```